Vietnam Recruitment Tour Postcard

We need a postcard to market a U.S. university student recruitment tour in northern Vietnam. The fair tour is organized by StudyBridgeAbroad which is a program of the Federal Office of Exchange www.studybridgeabroad.exchange-office.example

The audience for these postcards are U.S. higher education recruiters (not students). We want U.S. universities to sign up for the fair tour.

The postcards will be handed out at large education conferences.

Target Market(s)

U.S. university recruiters who are between the ages of 25 and 45.

Industry/Entity Type

University

Requirements
Must have
• Copy/Text: Please see attached doc. file for copy/text to be used on the front and back of the card.

Front: High color gloss

Back: Black and white only design

Featured Colors: Red, White, and Blue
- Should have a patriotic / U.S. government feel

Logos: Must use the attached Exchange Office logo and at least one StudyBridgeAbroad logo (can use more but not required)

```html
<!DOCTYPE html>
<html lang="en">
<head>
<meta charset="utf-8">
<title>Vietnam Recruitment Tour Postcard</title>
<link rel="stylesheet" href="https://fonts.googleapis.com/css2?family=Open+Sans:wght@300;400;600&family=Roboto+Condensed:wght@400;700&family=Archivo:wght@900&display=swap">
<style>
  :root {
    --page-bg: #e4e4e4;
    --card-dark: #2a2728;
    --flag-red: #c8202f;
    --flag-blue: #2b3a78;
    --white: #ffffff;
    --soft-white: #e8e8e8;
    --muted: #c9c2c4;
    --link-red: #e0303a;
    --logo-blue: #3f6fae;
    --ink: #111111;
    --rule: #d2d2d2;
  }
  * { margin: 0; padding: 0; box-sizing: border-box; }
  html, body { width: 1200px; height: 1000px; overflow: hidden; }
  body { background: var(--page-bg); position: relative; font-family: "Open Sans", sans-serif; }

  .postcard { position: absolute; left: 460px; width: 615px; height: 477px; overflow: hidden; }
  .postcard--front {
    top: 18px;
    background: linear-gradient(180deg, #3a3637 0%, #8c8889 42%, #4a4647 62%, var(--card-dark) 100%);
  }
  .postcard--back { top: 509px; height: 476px; background: var(--white); border: 1px solid #d0d0d0; }

  .front-flag {
    position: absolute; left: 0; top: 0; width: 615px; height: 200px;
    background:
      linear-gradient(180deg, rgba(0,0,0,0) 60%, rgba(120,116,117,0.9) 100%),
      linear-gradient(100deg, var(--flag-blue) 0%, #3b4f8f 30%, #d9d4d6 45%, var(--flag-red) 60%, #f3eaea 75%, #b53040 90%, #3a3637 100%);
  }
  .front-brand { position: absolute; left: 23px; top: 52px; color: var(--white); }
  .front-brand__name { font-size: 20px; font-weight: 400; letter-spacing: -0.2px; }
  .front-brand__note { font-size: 8px; font-weight: 400; color: var(--soft-white); margin-top: 2px; }

  .agency-mark { position: absolute; right: 20px; top: 17px; display: flex; align-items: center; gap: 10px; }
  .agency-mark__name { color: var(--white); font-size: 11px; font-weight: 600; text-align: right; width: 90px; line-height: 1.3; }
  .agency-mark__disc { width: 124px; height: 124px; border-radius: 50%; background: #1c1a1b; border: 3px solid var(--soft-white); }

  .front-copy { position: absolute; left: 0; width: 615px; text-align: center; color: var(--soft-white); }
  .front-copy--invite { top: 185px; font-size: 17px; font-weight: 300; color: var(--muted); }
  .front-copy--invite .accent { color: #d9868c; }
  .front-copy--title { top: 210px; font-size: 24px; font-weight: 300; color: var(--white); }
  .front-copy--dates { top: 310px; font-size: 12px; font-weight: 400; text-transform: uppercase; }
  .front-copy--dates .num { font-size: 21px; font-weight: 300; margin: 0 4px; }
  .front-copy--dates .dash { margin: 0 6px; }
  .front-copy--reg { top: 341px; font-size: 12.5px; }
  .front-copy--signup { top: 442px; font-size: 13px; }
  .front-copy--signup .link { color: var(--link-red); }

  .front-horizon { position: absolute; left: -60px; top: 412px; width: 735px; height: 200px; border-radius: 50%;
    background: radial-gradient(ellipse at 50% 0%, #5a2a2c 0%, #2b1f20 40%, #1a1718 100%);
    border-top: 2px solid #8a3a3c; }
  .front-mini-brand { position: absolute; left: 16px; top: 386px; color: var(--logo-blue); font-size: 15px; font-weight: 400; }

  .back-flag {
    position: absolute; left: 0; top: 0; width: 470px; height: 150px;
    background: linear-gradient(115deg, #cfcfcf 0%, #e6e6e6 35%, #f4f4f4 60%, rgba(255,255,255,0) 90%);
  }
  .back-copy { position: absolute; font-family: "Roboto Condensed", sans-serif; color: var(--ink); }
  .back-copy--headline { left: 16px; top: 12px; font-family: "Archivo", sans-serif; font-weight: 900; font-size: 19px; }
  .back-copy--lead { left: 16px; top: 36px; width: 362px; font-weight: 700; font-size: 10.5px; line-height: 14px; }
  .back-copy--note { left: 16px; top: 68px; font-size: 10px; letter-spacing: -0.2px; }
  .schedule { position: absolute; left: 78px; top: 87px; display: grid; grid-template-columns: 58px 161px 59px 120px; row-gap: 1px; font-family: "Roboto Condensed", sans-serif; font-size: 10px; line-height: 13px; color: var(--ink); }
  .back-copy--inquiry { left: 78px; top: 131px; font-size: 13px; }
  .back-copy--inquiry strong { font-size: 14.5px; font-weight: 700; margin-left: 2px; }

  .stamp-box { position: absolute; left: 467px; top: 19px; width: 116px; height: 138px; border: 1px solid #9a9a9a; }
  .address-divider { position: absolute; left: 297px; top: 152px; width: 1px; height: 324px; background: var(--rule); }
</style>
</head>
<body>

  <section class="postcard postcard--front" aria-label="Postcard front">
    <div class="front-flag" role="img" aria-label="Waving United States flag with stars and red and white stripes"></div>

    <div class="front-brand">
      <div class="front-brand__name">StudyBridgeAbroad</div>
      <div class="front-brand__note">Supported by the Federal Office of Exchange</div>
    </div>

    <div class="agency-mark">
      <div class="agency-mark__name">Federal Office of Exchange</div>
      <div class="agency-mark__disc"></div>
    </div>

    <p class="front-copy front-copy--invite">Join us in <span class="accent">VIETNAM</span> for the</p>
    <h1 class="front-copy front-copy--title">Off The Beaten Track (OTBT) Tour</h1>
    <p class="front-copy front-copy--dates">September<span class="num">29</span><span class="dash">–</span>October<span class="num">03</span></p>
    <p class="front-copy front-copy--reg">Registration is FREE &nbsp;-&nbsp; Limited Space</p>

    <div class="front-horizon"></div>
    <div class="front-mini-brand">StudyBridgeAbroad</div>
    <p class="front-copy front-copy--signup">Sign up today at <span class="link">sbabroad.example/otbt-vn</span></p>
  </section>

  <section class="postcard postcard--back" aria-label="Postcard back">
    <div class="back-flag" role="img" aria-label="Faint grey United States flag with stars"></div>

    <h2 class="back-copy back-copy--headline">Save the dates!</h2>
    <p class="back-copy back-copy--lead">Spend one week visiting northern Vietnam's best gifted and talented high schools that are "off the beaten track" of most U.S. recruiters.</p>
    <p class="back-copy back-copy--note">Tour will originate from and return to Hanoi Transportation provided by the Host Mission Office</p>

    <div class="schedule">
      <span>Sept 29 (Mo)</span><span>: Hung Yen &amp; Nam Dinh Provinces</span><span>Oct 2 (Th)</span><span>: Nghe An Province</span>
      <span>Sept 30 (Tu)</span><span>: Ninh Binh Province</span><span>Oct 3 (Fr)</span><span>: Thai Binh Province</span>
      <span>Oct 1 (We)</span><span>: Thanh Hoa Province</span><span></span><span></span>
    </div>

    <p class="back-copy back-copy--inquiry">For Inquiries Email: <strong>hanoi.tour@studybridgeabroad.example</strong></p>

    <div class="stamp-box"></div>
    <div class="address-divider"></div>
  </section>

</body>
</html>
```